Updated flyer

We've decided to do this as a house party, the info is below. For this you can use a model or not use one, either way is fine. I attached two logos and some designs we've used from sketch hive before. I also attached a pic with a duck that you can use as the background
RUN WILD
(Pool Party Edition)
July 13 2013
Featuring DJs
Marlo (logo) Tevan (logo)
Neil Hartwick Marcus Obreno
meetwallz.com/marlo87 for address (Natomas, invite only)
Full Bar/Food/Water Basketball/Pool Table/Fun
Reason: I changed the info since it's a house party now so I didn't want to rush to close. It is a guaranteed project though thx
21-40 year old house music lounge lovers
House

```html
<!DOCTYPE html>
<html lang="en">
<head>
<meta charset="utf-8">
<title>Run Wild – Pool Party Edition</title>
<link href="https://fonts.googleapis.com/css2?family=Archivo+Black&family=Arimo:wght@400;700&family=Fredoka:wght@600&family=Michroma&display=swap" rel="stylesheet">
<style>
  :root {
    --water-deep: #0b2a8f;
    --water-mid: #1f5fd6;
    --water-glow: #c9dcf6;
    --night: #07124a;
    --orange: #ff5a0a;
    --orange-dark: #c83c00;
    --white: #ffffff;
    --pool-blue: #2a86c8;
    --pool-edge: #d9e3ea;
    --badge-light: #5fb4ea;
    --badge-dark: #1a6fb8;
    --duck-light: #f7d04a;
    --duck-deep: #e8a818;
    --logo-blue: #2b58c4;
    --ring-grey: #9aa3b5;
  }
  html, body {
    margin: 0;
    padding: 0;
    overflow: hidden;
    background: var(--night);
  }
  .flyer {
    position: relative;
    width: 849px;
    height: 1200px;
    overflow: hidden;
    font-family: "Arimo", Arial, sans-serif;
    color: var(--white);
  }
  .flyer p { margin: 0; }
  .water {
    position: absolute;
    inset: 0;
    background:
      radial-gradient(ellipse 520px 300px at 270px 520px, var(--water-glow) 0%, rgba(120,170,240,0.6) 40%, rgba(31,95,214,0) 80%),
      linear-gradient(180deg, var(--water-deep) 0%, var(--water-mid) 35%, #2d6ad8 48%, var(--water-deep) 68%, var(--night) 85%, var(--night) 100%);
  }
  .headline {
    position: absolute;
    left: 42px;
    top: 50px;
    margin: 0;
    font-family: "Archivo Black", "Arial Black", sans-serif;
    font-size: 80px;
    line-height: 1;
    color: var(--orange);
    text-shadow: 2px 3px 0 var(--orange-dark), 0 0 6px rgba(255,255,255,0.5);
  }
  .date-badge {
    position: absolute;
    left: 560px;
    top: 30px;
    width: 258px;
    height: 258px;
    border-radius: 50%;
    border: 3px solid var(--white);
    background: radial-gradient(circle at 40% 30%, var(--badge-light) 0%, var(--badge-dark) 100%);
    box-shadow: 0 4px 12px rgba(0,0,0,0.45);
    box-sizing: border-box;
  }
  .date-badge__text {
    position: absolute;
    inset: 0;
    display: flex;
    flex-direction: column;
    align-items: center;
    justify-content: center;
    transform: rotate(-28deg);
    line-height: 1.1;
  }
  .date-badge__day { font-size: 32px; letter-spacing: 1px; }
  .date-badge__date { font-size: 40px; font-weight: 700; }
  .date-badge__rule { width: 180px; height: 2px; background: var(--white); margin: 5px 0; opacity: 0.85; }
  .date-badge__time { font-size: 32px; }
  .title {
    position: absolute;
    margin: 0;
    font-family: "Archivo Black", "Arial Black", sans-serif;
    color: var(--pool-blue);
    -webkit-text-stroke: 6px var(--pool-edge);
    paint-order: stroke fill;
    text-shadow: 3px 5px 0 rgba(40,60,90,0.55);
    line-height: 1;
  }
  .title--pool {
    left: 58px;
    top: 300px;
    font-size: 150px;
    letter-spacing: -2px;
    transform: rotate(-5deg);
  }
  .title--party {
    left: 140px;
    top: 420px;
    font-size: 168px;
    letter-spacing: 0;
    transform: rotate(-10deg);
  }
  .duck-placeholder {
    position: absolute;
    left: 519px;
    top: 242px;
    width: 156px;
    height: 190px;
    border-radius: 24px;
    background: linear-gradient(180deg, var(--duck-light) 0%, var(--duck-deep) 100%);
  }
  .edition {
    position: absolute;
    left: 548px;
    top: 582px;
    font-family: "Fredoka", sans-serif;
    font-weight: 600;
    font-size: 68px;
    letter-spacing: 2px;
    line-height: 1;
    color: var(--white);
    text-shadow: 2px 3px 2px rgba(0,0,0,0.45);
  }
  .line {
    position: absolute;
    left: 40px;
    line-height: 1;
    white-space: nowrap;
  }
  .with { top: 676px; font-size: 42px; }
  .caps { font-family: "Michroma", sans-serif; letter-spacing: 2px; }
  .caps small { font-size: 0.78em; }
  .lineup-label { top: 742px; font-size: 34px; }
  .accent { color: var(--orange); }
  .dj { left: 76px; font-size: 35px; color: var(--orange); }
  .dj--first { top: 786px; }
  .dj--second { top: 834px; }
  .amenities { font-size: 28px; }
  .amenities--first { top: 888px; }
  .amenities--second { top: 936px; }
  .address { top: 974px; font-size: 33px; color: var(--orange); }
  .brand-marlo {
    position: absolute;
    left: 296px;
    top: 1066px;
    font-family: "Archivo Black", "Arial Black", sans-serif;
    font-size: 70px;
    letter-spacing: 4px;
    line-height: 1;
    color: var(--logo-blue);
  }
  .brand-tevan {
    position: absolute;
    left: 651px;
    top: 1008px;
    width: 172px;
    height: 172px;
    border-radius: 50%;
    border: 2px solid var(--ring-grey);
    box-sizing: border-box;
    display: flex;
    align-items: center;
    justify-content: center;
    font-family: "Archivo Black", "Arial Black", sans-serif;
    font-size: 34px;
    color: var(--white);
  }
</style>
</head>
<body>
<main class="flyer">
  <div class="water" role="img" aria-label="Rippling blue pool water background"></div>

  <h1 class="headline">RUN WILD</h1>

  <div class="date-badge">
    <div class="date-badge__text">
      <span class="date-badge__day">SATURDAY</span>
      <span class="date-badge__date">07/13/2013</span>
      <span class="date-badge__rule"></span>
      <span class="date-badge__time">10pm - 2pm</span>
    </div>
  </div>

  <h2 class="title title--pool">POOL</h2>
  <div class="duck-placeholder" role="img" aria-label="Rubber duck mascot floating in a swim ring"></div>
  <h2 class="title title--party">PARTY</h2>
  <p class="edition">EDITION</p>

  <p class="line with">with</p>
  <p class="line caps lineup-label">F<small>EATURING</small> <span class="accent">DJ</span><small>s</small></p>
  <p class="line caps dj dj--first">N<small>EIL</small> H<small>ARTWICK</small></p>
  <p class="line caps dj dj--second">M<small>ARCUS</small> O<small>BRENO</small></p>
  <p class="line caps amenities amenities--first"><span class="accent">F<small>ULL</small></span> B<small>AR</small>/F<small>OOD</small>/W<small>ATER</small> B<small>ASKETBALL</small></p>
  <p class="line caps amenities amenities--second">P<small>OOL</small> T<small>ABLE</small>/F<small>UN</small></p>
  <p class="line address">meetwallz.com/marlo87 for address</p>

  <div class="brand-marlo">MARLO</div>
  <div class="brand-tevan">TEVAN</div>
</main>
</body>
</html>
```